Tamarack Hearth Partners Business Card

Looking for a new business card layout. We are a real estate firm w/ a logo, old design attached. Must keep the same elements on there, just need a fresh look and possible some foil accents. Looking for a simpler design w/ more modern style.

Target Market(s)

Real Estate clients

Industry/Entity Type

Real Estate Agent

Contact Information for Business Card

see attached

Font styles to use
Sans Serif

Requirements
Must have
• all elements on current biz card
Nice to have
• modern look, simpler than we have!
Should not have
• no serif fonts

```html
<!DOCTYPE html>
<html lang="en">
<head>
<meta charset="utf-8">
<title>Tamarack Hearth Partners – Business Card</title>
<link rel="stylesheet" href="https://fonts.googleapis.com/css2?family=Arimo:wght@400;700&display=swap">
<style>
  :root {
    --charcoal: #414142;
    --citron: #dccb13;
    --signal-red: #e21d24;
    --white: #ffffff;
    --photo-light: #f4f1ee;
    --photo-mid: #d9b9a8;
    --photo-teal: #5fe0bf;
  }
  * { margin: 0; padding: 0; box-sizing: border-box; }
  html, body { width: 1200px; height: 668px; overflow: hidden; background: var(--white); }
  .card {
    position: relative;
    width: 1200px;
    height: 668px;
    background: var(--charcoal);
    font-family: "Arimo", Arial, sans-serif;
    color: var(--white);
    overflow: hidden;
  }
  .card__shapes { position: absolute; inset: 0; }
  .info {
    position: absolute;
    right: 49px;
    text-align: right;
    white-space: nowrap;
    line-height: 1;
  }
  .agent-name { top: 54px; font-size: 54px; font-weight: 700; letter-spacing: 0.5px; }
  .agent-title { top: 107px; font-size: 30px; }
  .phone { font-size: 35px; }
  .phone strong { font-weight: 700; }
  .phone--office { top: 187px; }
  .phone--cell { top: 235px; }
  .contact { font-size: 34px; }
  .contact--email { top: 300px; }
  .contact--web { top: 350px; }
  .contact--street { top: 417px; }
  .contact--city { top: 461px; }
  .brand {
    top: 562px;
    height: 56px;
    display: flex;
    align-items: center;
    gap: 22px;
  }
  .brand__mark {
    width: 50px;
    height: 50px;
    background: var(--white);
    flex: none;
  }
  .brand__name { font-size: 40px; font-weight: 700; }
</style>
</head>
<body>
  <div class="card">
    <svg class="card__shapes" width="1200" height="668" viewBox="0 0 1200 668">
      <defs>
        <linearGradient id="portrait-tones" x1="0" y1="0" x2="0" y2="1">
          <stop offset="0" stop-color="var(--photo-light)"/>
          <stop offset="0.55" stop-color="var(--photo-mid)"/>
          <stop offset="1" stop-color="var(--photo-teal)"/>
        </linearGradient>
        <filter id="soft-shadow" x="-20%" y="-20%" width="140%" height="140%">
          <feDropShadow dx="8" dy="10" stdDeviation="14" flood-color="#000" flood-opacity="0.45"/>
        </filter>
      </defs>
      <polygon class="accent-chevron" points="0,0 417,0 231,334 417,668 0,668" fill="var(--citron)"/>
      <rect class="rule rule--top" x="440" y="155" width="711" height="6" fill="var(--signal-red)"/>
      <rect class="rule rule--bottom" x="440" y="510" width="711" height="6" fill="var(--signal-red)"/>
      <polygon class="portrait" role="img" aria-label="Portrait photo of the broker"
               points="90,334 197,138 434,138 541,334 434,530 197,530"
               fill="url(#portrait-tones)" filter="url(#soft-shadow)"/>
    </svg>

    <div class="info agent-name">MARLA QUINN</div>
    <div class="info agent-title">Principal Broker</div>

    <div class="info phone phone--office">Office <strong>555-210-4870</strong></div>
    <div class="info phone phone--cell">Cell <strong>555-318-6624</strong></div>

    <div class="info contact contact--email">marla@tamarackhearth.com</div>
    <div class="info contact contact--web">TamarackHearthHomes.com</div>
    <div class="info contact contact--street">482 Juniper Ridge Ave</div>
    <div class="info contact contact--city">Pine Hollow, OR 97000</div>

    <div class="info brand">
      <span class="brand__mark" aria-hidden="true"></span>
      <span class="brand__name">Tamarack Hearth Partners</span>
    </div>
  </div>
</body>
</html>
```